The Bloom Company Sweet Packaging Design

The Lagoon Bloom Company is looking for a logo and label design for an upcoming line of honey based health and beauty products that are sourced from the Polynesian Islands (Hawaii, New Zealand, Fiji etc.).The brand will be premium price positioned and the design and packaging should exude class and quality.The design should be flexible enough to add products from future locations.We would like to see the design across three different product forms:1. Glass Honey Jar (main product)2. Hand cream / lotion (pump bottle, or lotion tube)3. Small box (e.g. throat lozenges / gum packet etc.)The Polynesia Islands are unique and exotic locations; the design/packaging should reflect this but should not be overly complicated. Each individual island has their own distinct culture and history but they have many commonalities which fall under "Polynesian Culture". The Lagoon Bloom Company is an umbrella brand that should be able to support a growing number of products.Possible designs may (but are not required to) incorporate local flowers (Hawaii / Hibiscus flower, New Zealand / Manuka Flower etc.) into the design, Islands, and boutique feel (elegant classy looking)Please feel free to ask more questions for further guidance but we really want to see where the creative process can take us outside of what we have already considered internally.
Updates

We needed to modify our idea slightly because of competition.

We needed extend to get a few more ideas. We did not want to copy our competition and needed to add a part to our design that we did not include before.

Target Market(s)

Health conscious people. Honey lovers.

Font styles to use
Serif
Sans Serif
Decorative

Colors

Designer to choose colors to be used in the design.

Requirements
Must have
• a little tribal look. because its 100% polynesian Honey.. it would be nice to have the fee of that in the design..

```html
<!DOCTYPE html>
<html lang="en">
<head>
<meta charset="utf-8">
<title>The Lagoon Bloom Company – Manuka Label</title>
<link rel="stylesheet" href="https://fonts.googleapis.com/css2?family=Montserrat:wght@800&family=Oswald:wght@700&family=Allura&family=Questrial&display=swap">
<style>
  :root {
    --gold: #edb21f;
    --gold-deep: #8a6410;
    --ink: #000000;
    --white: #ffffff;
    --paper: #ffffff;
  }
  * { margin: 0; padding: 0; box-sizing: border-box; }
  html, body {
    width: 1059px;
    height: 1200px;
    overflow: hidden;
    background: var(--paper);
  }
  .canvas {
    position: relative;
    width: 1059px;
    height: 1200px;
  }
  .label {
    position: absolute;
    left: 50px;
    top: 148px;
    width: 960px;
    height: 907px;
    background: var(--gold);
    overflow: hidden;
  }
  .label__art {
    position: absolute;
    inset: 0;
    width: 960px;
    height: 907px;
  }
  .brand-arc {
    font-family: "Montserrat", sans-serif;
    font-weight: 800;
    font-size: 60px;
    letter-spacing: 22px;
    fill: var(--ink);
  }
  .brand-main {
    position: absolute;
    left: 0;
    right: 0;
    top: 392px;
    text-align: center;
    font-family: "Oswald", sans-serif;
    font-weight: 700;
    font-size: 118px;
    line-height: 1;
    color: var(--gold);
    letter-spacing: 1px;
  }
  .brand-sub {
    position: absolute;
    left: 0;
    right: 0;
    top: 505px;
    text-align: center;
    font-family: "Montserrat", sans-serif;
    font-weight: 800;
    font-size: 31px;
    line-height: 1;
    color: var(--gold);
  }
  .flower-spray {
    position: absolute;
    top: 454px;
    width: 188px;
    height: 343px;
    border-radius: 30px;
    background: radial-gradient(circle at 50% 50%, #dcdcdc 0%, #ffffff 75%);
  }
  .flower-spray--left { left: 64px; }
  .flower-spray--right { left: 717px; }
  .product-name {
    position: absolute;
    left: 0;
    right: 0;
    top: 532px;
    text-align: center;
    font-family: "Allura", cursive;
    font-size: 132px;
    line-height: 1;
    color: var(--white);
  }
  .net-weight {
    position: absolute;
    left: 0;
    right: 0;
    top: 698px;
    text-align: center;
    font-family: "Questrial", sans-serif;
    font-size: 30px;
    letter-spacing: 1px;
    line-height: 1;
    color: var(--white);
  }
  .pattern-band {
    position: absolute;
    left: 14px;
    right: 14px;
    top: 834px;
    height: 73px;
    background: linear-gradient(90deg, var(--gold) 0%, var(--gold-deep) 25%, var(--gold) 50%, var(--gold-deep) 75%, var(--gold) 100%);
  }
</style>
</head>
<body>
<main class="canvas">
  <section class="label">
    <svg class="label__art" viewBox="0 0 960 907" aria-hidden="false">
      <defs>
        <radialGradient id="emblem-tone" cx="50%" cy="100%" r="100%">
          <stop offset="0%" stop-color="#edb21f"/>
          <stop offset="55%" stop-color="#b8870f"/>
          <stop offset="100%" stop-color="#000000"/>
        </radialGradient>
        <path id="brand-curve" d="M 53 584 A 427 427 0 0 1 907 584"/>
      </defs>
      <path d="M0 335 Q480 520 960 335 L960 907 L0 907 Z" fill="var(--ink)"/>
      <path d="M218 431 A262 262 0 0 1 742 431 Z" fill="url(#emblem-tone)" role="img" aria-label="Tribal arch emblem with a bee at its centre"/>
      <text class="brand-arc" text-anchor="middle">
        <textPath href="#brand-curve" startOffset="50%">THE LAGOON</textPath>
      </text>
    </svg>
    <p class="brand-main">BLOOM</p>
    <p class="brand-sub">COMPANY</p>
    <div class="flower-spray flower-spray--left" role="img" aria-label="White hibiscus flower spray illustration"></div>
    <div class="flower-spray flower-spray--right" role="img" aria-label="White hibiscus flower spray illustration"></div>
    <p class="product-name">Manuka</p>
    <p class="net-weight">8.8 oz | 250 gsm</p>
    <div class="pattern-band" role="img" aria-label="Gold and black tribal triangle pattern band"></div>
  </section>
</main>
</body>
</html>
```